Fretwise Riff Hall WebSite

I am looking for a website design for FretwiseRiffHall.com. If you are unfamiliar with the term "guitar lick": a guitar lick is a simple piece of music that is used in an improvisation or solo. All of the famous guitarists that you probably have heard of (Tobin Marlowe, Dale Pemberly, etc.) have their own set of unique licks. This is what defines their style. The "Dojo" in the site name refers to a karate dojo. Basically, like a person would master karate in a karate dojo, a guitarist can master guitar licks in the Fretwise Riff Hall. The purpose of FretwiseRiffHall is to show users very high quality videos (vidstreamo) and music notation for a variety of licks. Many of the guitar licks on the site will be from famous guitarists. There will also be licks that are not from famous guitarists, that are just general licks in a particular style or genre.

Target Market(s)

Intermediate and above guitar players.

Industry/Entity Type

Vidstreamo

Requirements
Must have
• 1) The look and feel of the site must be based on the logo that I have attached. First and foremost, this site must be FUN. The page should fit with the mood of the logo. The logo should be incorporated well into the header design. It would be nice to see the logo theme used throughout the same page in some creative and reasonable way.
• 2) There will be three main navigation tabs on the home page: Licks, JamTracks, and Blog. The Licks section will be broken into Licks by Artist, and licks by genre (eg. Jazz, Rock, Blues, Fusion, Heavy Metal, Country, etc.)
• 3) There needs to be 3 main sections on the Home Page: Lick of the Day, Recently Added Licks, and Featured Licks. These 3 sections must contain thumbnails of the videos, along with a text description.
Nice to have
• Use the character from the logo or the karate theme in some creative way on the page.

```html
<!DOCTYPE html>
<html lang="en">
<head>
<meta charset="utf-8">
<title>Fretwise Riff Hall</title>
<link rel="stylesheet" href="https://fonts.googleapis.com/css2?family=Arvo:wght@400;700&family=PT+Serif:wght@400;700&family=Open+Sans:wght@400;600;700&display=swap">
<style>
:root{
  --cyan:#19b9e8;
  --cyan-light:#6ddcf7;
  --cyan-deep:#0a8fc4;
  --black:#0b0b0b;
  --red:#ec1f2d;
  --page:#f2f2f2;
  --ink:#1b1b1b;
  --body-ink:#333333;
  --card:#151515;
  --card-band:#222222;
  --muted:#6d6d6d;
  --rule:#53b6dd;
  --footer:#333333;
  --footer-ink:#c9c9c9;
  --white:#ffffff;
}
*{margin:0;padding:0;box-sizing:border-box}
html,body{width:1200px;height:2894px;overflow:hidden}
body{position:relative;background:var(--page);font-family:"PT Serif",Georgia,serif;color:var(--body-ink)}
.abs{position:absolute}

/* Header */
.hero{left:0;top:0;width:1200px;height:608px;background:radial-gradient(ellipse at 45% 55%,var(--cyan-light) 0%,var(--cyan) 45%,var(--cyan-deep) 100%);overflow:hidden}
.hero-photo{right:0;top:77px;width:718px;height:531px;background:radial-gradient(ellipse at 62% 45%,#5a4a40 0%,#2b2623 38%,rgba(25,185,232,0) 70%)}
.navbar{left:0;top:89px;width:1200px;height:46px;background:var(--black)}
.nav{left:422px;top:89px;display:flex;height:54px}
.nav a{font-family:"PT Serif",Georgia,serif;font-size:13px;color:var(--white);text-decoration:none;text-transform:uppercase;display:flex;align-items:center;height:46px;padding:0 22px;margin-right:36px;letter-spacing:.3px}
.nav a.active{background:var(--red);height:54px;padding:0 18px;margin-right:44px}
.brand{left:172px;top:0;width:226px;height:212px}
.brand-disc{left:0;top:0;width:212px;height:212px;border-radius:50%;background:#0d2236}
.brand-name{left:-6px;top:140px;width:226px;text-align:center;font-family:"Arvo",Georgia,serif;font-weight:700;font-size:22px;color:var(--white)}
.socials{left:768px;top:36px;display:flex;gap:10px}
.socials span{width:24px;height:24px;border-radius:50%;border:2px solid var(--white)}
.btn{font-family:"PT Serif",Georgia,serif;font-size:12px;text-transform:uppercase;color:var(--white);background:var(--red);display:flex;align-items:center;justify-content:center;text-decoration:none}
.signup{left:912px;top:33px;width:94px;height:33px;font-size:13px}
.hero-title{left:199px;top:256px;font-family:"Arvo",Georgia,serif;font-weight:700;font-size:48px;line-height:52px;color:var(--black);letter-spacing:1px}
.hero-text{left:199px;top:366px;width:460px;font-family:"Open Sans",Arial,sans-serif;font-size:15px;line-height:24px;color:var(--black)}
.learn{left:199px;top:440px;width:120px;height:36px}
.watch{left:332px;top:440px;width:119px;height:36px;background:transparent;border:1px solid var(--white)}

/* Lick of the day */
.lotd-title{left:150px;top:676px;font-family:"Arvo",Georgia,serif;font-weight:700;font-size:32px;line-height:38px;color:var(--ink)}
.red{color:var(--red)}
.lotd-text{left:150px;top:774px;width:300px;font-size:13px;line-height:21px;color:var(--body-ink)}
.lotd-btn{left:150px;top:999px;width:121px;height:39px}
.video{left:525px;top:667px;width:529px;height:382px;background:var(--black)}
.video-frame{left:0;top:0;width:529px;height:324px;background:radial-gradient(ellipse at 40% 40%,#6a5a4a 0%,#2f3550 55%,#121212 100%)}
.video-progress{left:0;top:324px;width:529px;height:3px;background:#3a3a3a}
.video-progress i{display:block;width:210px;height:3px;background:var(--red)}
.video-controls{left:0;top:327px;width:529px;height:55px;display:flex;align-items:center;font-family:"Open Sans",Arial,sans-serif;font-size:10px;color:#d0d0d0}
.time{position:absolute;left:76px}
.time b{font-weight:400;color:#8a8a8a}
.vol{position:absolute;left:370px;top:21px;width:58px;height:3px;background:var(--red);top:26px}

/* Sections */
.rule{left:0;width:1200px;height:2px;background:var(--rule)}
.sec-title{left:0;width:1200px;text-align:center;font-family:"Arvo",Georgia,serif;font-weight:700;font-size:32px;color:var(--ink);letter-spacing:.5px}
.sec-text{left:150px;width:900px;font-size:12.5px;line-height:23px;color:var(--body-ink)}
.cards{left:160px;display:flex;gap:28px}
.card{width:197px;height:293px;background:var(--card);position:relative}
.card-img{width:197px;height:218px;position:relative}
.card-img.warm{background:linear-gradient(160deg,#c9772f 0%,#7a3320 50%,#2a1a14 100%)}
.card-img.dark{background:linear-gradient(160deg,#3c3026 0%,#8c7664 50%,#1d1712 100%)}
.card-img.violet{background:linear-gradient(160deg,#4b3f7a 0%,#7b5f86 45%,#1b1430 100%)}
.play{position:absolute;left:58px;top:64px}
.card-band{height:37px;background:var(--card-band);display:flex;align-items:center;padding-left:12px;font-size:12px;text-transform:uppercase;color:var(--red);gap:8px}
.card-text{padding:3px 12px 0;font-size:12px;line-height:15px;color:#555}
.dots{left:0;width:1200px;display:flex;justify-content:center;gap:10px}
.dots span{width:11px;height:11px;border-radius:50%;background:var(--black)}
.dots span.half{background:linear-gradient(90deg,var(--black) 50%,var(--page) 50%);border:1px solid var(--black)}

/* Blog */
.posts{left:149px;top:2371px;display:flex;gap:17px}
.post{width:445px;height:156px;background:var(--card);position:relative}
.post-date{position:absolute;left:22px;top:44px;font-family:"Open Sans",Arial,sans-serif;color:#a9a9a9}
.post-date small{display:block;font-size:16px;letter-spacing:-.5px}
.post-date strong{display:block;font-size:29px;font-weight:600;line-height:30px}
.post-bar{position:absolute;left:113px;top:30px;width:5px;height:98px;background:var(--red)}
.post-title{position:absolute;left:140px;top:28px;font-family:"Open Sans",Arial,sans-serif;font-weight:600;font-size:15px;color:var(--white)}
.post-text{position:absolute;left:140px;top:54px;width:270px;font-family:"Open Sans",Arial,sans-serif;font-size:13px;line-height:17px;color:#6a6a6a}

/* Footer */
.footer{left:0;top:2614px;width:1200px;height:280px;background:var(--footer);border-top:3px solid var(--rule);font-family:"Open Sans",Arial,sans-serif;color:var(--footer-ink)}
.f-head{position:absolute;top:35px;font-size:13px;font-weight:700;text-transform:uppercase;color:var(--white);display:flex;align-items:center;gap:6px}
.links{position:absolute;left:148px;top:76px;list-style:none;font-size:12px;line-height:18.5px}
.f-social{position:absolute;left:148px;top:212px;display:flex;gap:14px}
.f-social span{width:25px;height:25px;border-radius:50%;border:2px solid #bdbdbd;display:flex;align-items:center;justify-content:center}
.comment{position:absolute;left:380px;width:320px;display:flex;gap:12px}
.avatar{width:48px;height:48px;background:#e6e6e6;flex:none}
.comment p{font-size:10.5px;line-height:15px;font-style:italic;color:var(--footer-ink)}
.comment p em{color:var(--red)}
.news-text{position:absolute;left:748px;top:70px;width:300px;font-size:12px;line-height:18px}
.news-input{position:absolute;left:748px;top:135px;width:291px;height:37px;border:1px solid #5a5a5a;font-size:11px;color:#aaa;padding:10px 12px}
.submit{position:absolute;left:908px;top:183px;width:130px;height:36px;font-family:"Open Sans",Arial,sans-serif;font-weight:700;font-size:14px}
</style>
</head>
<body>

<header>
  <div class="abs hero">
    <div class="abs hero-photo" role="img" aria-label="Rock guitarist in cap and sunglasses playing an orange sunburst electric guitar against a burst of light and swirling music notes"></div>
  </div>
  <div class="abs navbar"></div>
  <nav class="abs nav">
    <a class="active" href="#">Home</a>
    <a href="#">Artist Licks</a>
    <a href="#">General Licks</a>
    <a href="#">Blog</a>
    <a href="#">Contact</a>
  </nav>
  <div class="abs brand">
    <div class="abs brand-disc"></div>
    <div class="abs brand-name">FretwiseRiffHall</div>
  </div>
  <div class="abs socials"><span></span><span></span><span></span><span></span></div>
  <a class="abs btn signup" href="#">Sign Up</a>
  <h1 class="abs hero-title">Welcome To<br>FretwiseRiffHall</h1>
  <p class="abs hero-text">Lorem ipsum dolor sit amet, consectetur adipiscing elit. Etiam pretium, nibh ac scelerisque tincidunt.</p>
  <a class="abs btn learn" href="#">Learn More</a>
  <a class="abs btn watch" href="#">Watch Videos</a>
</header>

<section class="lick-of-the-day">
  <h2 class="abs lotd-title">LICK<br><span class="red">OF THE DAY</span></h2>
  <p class="abs lotd-text">Lorem ipsum dolor sit amet, consectetur adipiscing elit. Etiam pretium, nibh ac scelerisque tincidunt, risus quam scelerisque ante, non finibus ex diam vel orci. Maecenas accumsan eros in eros rutrum elementum. Curabitur molestie tristique finibus In rutrum lobortis est non auctor. Mauris vehicula id nunc ac dapibus.Curabitur pharetra sapien vitae urna euismod dictum. Mauris iaculis est mi, egestas congue...</p>
  <a class="abs btn lotd-btn" href="#">Learn More</a>
  <div class="abs video">
    <div class="abs video-frame" role="img" aria-label="Guitarist performing on stage under blue lights"></div>
    <svg class="abs" style="left:204px;top:102px" width="122" height="122" viewBox="0 0 122 122"><circle cx="61" cy="61" r="56" fill="none" stroke="#fff" stroke-opacity=".8" stroke-width="8"/><path d="M46 34 L92 61 L46 88Z" fill="#fff" fill-opacity=".8"/></svg>
    <div class="abs video-progress"><i></i></div>
    <div class="abs video-controls">
      <svg style="position:absolute;left:22px;top:21px" width="12" height="14"><rect width="4" height="14" fill="#ddd"/><rect x="8" width="4" height="14" fill="#ddd"/></svg>
      <span class="time">00:54:21 <b>/ 01:42:30</b></span>
      <svg style="position:absolute;left:349px;top:18px" width="12" height="18" viewBox="0 0 12 18"><path d="M4 2 V13" stroke="#ddd" stroke-width="2"/><ellipse cx="3" cy="14" rx="3" ry="2.5" fill="#ddd"/><path d="M4 2 L10 5" stroke="#ddd" stroke-width="2"/></svg>
      <span class="vol"></span>
      <svg style="position:absolute;left:492px;top:19px" width="16" height="16" viewBox="0 0 16 16" fill="none" stroke="#ddd" stroke-width="2"><path d="M1 5V1H5M11 1H15V5M15 11V15H11M5 15H1V11M1 1L6 6M15 1L10 6M15 15L10 10M1 15L6 10"/></svg>
    </div>
  </div>
</section>

<div class="abs rule" style="top:1102px"></div>

<section class="recent-licks">
  <h2 class="abs sec-title" style="top:1140px">RECENTLY <span class="red">ADDED LICKS</span></h2>
  <p class="abs sec-text" style="top:1200px">Lorem ipsum dolor sit amet, consectetur adipiscing elit. Etiam pretium, nibh ac scelerisque tincidunt, risus quam scelerisque ante, non finibus ex diam vel orci. Maecenas accumsan eros in eros rutrum elementum. Curabitur molestie tristique finibus. In rutrum lobortis est non auctor. Mauris vehicula id nunc ac dapibus. Curabitur pharetra sapien vitae urna euismod dictum. Mauris iaculis est mi, egestas congue neque mollis vitae. Suspendisse potenti. Morbi a odio vitae sem efficitur pellentesque sed in tellus.</p>
  <div class="abs cards" style="top:1312px">
    <article class="card"><div class="card-img warm" role="img" aria-label="Guitarist in a patterned jacket playing guitar"><svg class="play" width="80" height="80" viewBox="0 0 80 80"><circle cx="40" cy="40" r="35" fill="none" stroke="#fff" stroke-opacity=".8" stroke-width="6"/><path d="M30 22 L58 40 L30 58Z" fill="#fff" fill-opacity=".8"/></svg></div><div class="card-band">Tobin Marlowe Album</div><p class="card-text">Lorem ipsum dolor sit amet, consectetur</p></article>
    <article class="card"><div class="card-img dark" role="img" aria-label="Guitarist in a white jacket playing guitar"><svg class="play" width="80" height="80" viewBox="0 0 80 80"><circle cx="40" cy="40" r="35" fill="none" stroke="#fff" stroke-opacity=".8" stroke-width="6"/><path d="M30 22 L58 40 L30 58Z" fill="#fff" fill-opacity=".8"/></svg></div><div class="card-band">&#9835; Tobin Marlowe Album</div><p class="card-text">Lorem ipsum dolor sit amet, consectetur</p></article>
    <article class="card"><div class="card-img violet" role="img" aria-label="Guitarist playing under purple stage light"><svg class="play" width="80" height="80" viewBox="0 0 80 80"><circle cx="40" cy="40" r="35" fill="none" stroke="#fff" stroke-opacity=".8" stroke-width="6"/><path d="M30 22 L58 40 L30 58Z" fill="#fff" fill-opacity=".8"/></svg></div><div class="card-band">&#9835; Tobin Marlowe Album</div><p class="card-text">Lorem ipsum dolor sit amet, consectetur</p></article>
    <article class="card"><div class="card-img dark" role="img" aria-label="Guitarist in a white jacket playing guitar"><svg class="play" width="80" height="80" viewBox="0 0 80 80"><circle cx="40" cy="40" r="35" fill="none" stroke="#fff" stroke-opacity=".8" stroke-width="6"/><path d="M30 22 L58 40 L30 58Z" fill="#fff" fill-opacity=".8"/></svg></div><div class="card-band">&#9835; Tobin Marlowe Album</div><p class="card-text">Lorem ipsum dolor sit amet, consectetur</p></article>
  </div>
  <div class="abs dots" style="top:1650px"><span class="half"></span><span></span><span></span><span></span></div>
</section>

<div class="abs rule" style="top:1695px"></div>

<section class="popular-licks">
  <h2 class="abs sec-title" style="top:1723px">MOST <span class="red">POPULAR LICKS</span></h2>
  <p class="abs sec-text" style="top:1782px">Lorem ipsum dolor sit amet, consectetur adipiscing elit. Etiam pretium, nibh ac scelerisque tincidunt, risus quam scelerisque ante, non finibus ex diam vel orci. Maecenas accumsan eros in eros rutrum elementum. Curabitur molestie tristique finibus. In rutrum lobortis est non auctor. Mauris vehicula id nunc ac dapibus. Curabitur pharetra sapien vitae urna euismod dictum. Mauris iaculis est mi, egestas congue neque mollis vitae. Suspendisse potenti. Morbi a odio vitae sem efficitur pellentesque sed in tellus.</p>
  <div class="abs cards" style="top:1894px;left:164px">
    <article class="card"><div class="card-img warm" role="img" aria-label="Guitarist in a patterned jacket playing guitar"><svg class="play" width="80" height="80" viewBox="0 0 80 80"><circle cx="40" cy="40" r="35" fill="none" stroke="#fff" stroke-opacity=".8" stroke-width="6"/><path d="M30 22 L58 40 L30 58Z" fill="#fff" fill-opacity=".8"/></svg></div><div class="card-band">Tobin Marlowe Album</div><p class="card-text">Lorem ipsum dolor sit amet, consectetur</p></article>
    <article class="card"><div class="card-img dark" role="img" aria-label="Guitarist in a white jacket playing guitar"><svg class="play" width="80" height="80" viewBox="0 0 80 80"><circle cx="40" cy="40" r="35" fill="none" stroke="#fff" stroke-opacity=".8" stroke-width="6"/><path d="M30 22 L58 40 L30 58Z" fill="#fff" fill-opacity=".8"/></svg></div><div class="card-band">&#9835; Tobin Marlowe Album</div><p class="card-text">Lorem ipsum dolor sit amet, consectetur</p></article>
    <article class="card"><div class="card-img violet" role="img" aria-label="Guitarist playing under purple stage light"><svg class="play" width="80" height="80" viewBox="0 0 80 80"><circle cx="40" cy="40" r="35" fill="none" stroke="#fff" stroke-opacity=".8" stroke-width="6"/><path d="M30 22 L58 40 L30 58Z" fill="#fff" fill-opacity=".8"/></svg></div><div class="card-band">&#9835; Tobin Marlowe Album</div><p class="card-text">Lorem ipsum dolor sit amet, consectetur</p></article>
    <article class="card"><div class="card-img dark" role="img" aria-label="Guitarist in a white jacket playing guitar"><svg class="play" width="80" height="80" viewBox="0 0 80 80"><circle cx="40" cy="40" r="35" fill="none" stroke="#fff" stroke-opacity=".8" stroke-width="6"/><path d="M30 22 L58 40 L30 58Z" fill="#fff" fill-opacity=".8"/></svg></div><div class="card-band">&#9835; Tobin Marlowe Album</div><p class="card-text">Lorem ipsum dolor sit amet, consectetur</p></article>
  </div>
  <div class="abs dots" style="top:2223px"><span class="half"></span><span></span><span></span><span></span></div>
</section>

<div class="abs rule" style="top:2269px"></div>

<section class="blog">
  <h2 class="abs sec-title" style="top:2301px">RECENT <span class="red">BLOGPOSTS</span></h2>
  <div class="abs posts">
    <article class="post"><div class="post-date"><small>24 AUG</small><strong>2014</strong></div><span class="post-bar"></span><h3 class="post-title">Thousands celebrities at Johnnie Night</h3><p class="post-text">Lorem ipsum dolor sit amet, consect ictum. Lorem ipsum dolor sit amet, consect etur ictum.</p></article>
    <article class="post"><div class="post-date"><small>24 AUG</small><strong>2014</strong></div><span class="post-bar"></span><h3 class="post-title">Thousands celebrities at Johnnie Night</h3><p class="post-text">Lorem ipsum dolor sit amet, consect ictum. Lorem ipsum dolor sit amet, consect etur ictum.</p></article>
  </div>
  <div class="abs dots" style="top:2566px"><span class="half"></span><span></span><span></span><span></span></div>
</section>

<footer class="abs footer">
  <h4 class="f-head" style="left:135px"><svg width="10" height="14" viewBox="0 0 10 14"><path d="M6 0 L0 8 H4 L3 14 L10 5 H6Z" fill="#fff"/></svg>Quick Links</h4>
  <ul class="links"><li>Home</li><li>About Us</li><li>Licks</li><li>Jamtracks</li><li>Blog</li><li>Contact Us</li></ul>
  <div class="f-social"><span></span><span></span><span><svg width="13" height="9" viewBox="0 0 13 9"><rect width="13" height="9" fill="#bdbdbd"/><path d="M0 0 L6.5 5 L13 0" fill="none" stroke="#333" stroke-width="1.2"/></svg></span><span></span><span></span></div>

  <h4 class="f-head" style="left:380px"><svg width="12" height="12" viewBox="0 0 12 12"><circle cx="6" cy="3.5" r="3" fill="#fff"/><path d="M0 12 C0 7 12 7 12 12Z" fill="#fff"/></svg>Customer Comments</h4>
  <div class="comment" style="top:70px"><div class="avatar"></div><p><em>Posted 14 days ago</em><br>Lorem ipsum dolor sit amet consectetur adipiscing elit, Sed do eiusmod tempor incidunt ut labore et dolore magna aliqua..</p></div>
  <div class="comment" style="top:158px"><div class="avatar"></div><p><em>Posted 14 days ago</em><br>Lorem ipsum dolor sit amet consectetur adipiscing elit, Sed do eiusmod tempor incidunt ut labore et dolore magna aliqua..</p></div>

  <h4 class="f-head" style="left:748px"><svg width="14" height="10" viewBox="0 0 14 10"><rect x=".5" y=".5" width="13" height="9" fill="none" stroke="#fff"/><path d="M.5 .5 L7 6 L13.5 .5" fill="none" stroke="#fff"/></svg>Newsletter</h4>
  <p class="news-text">Lorem ipsum dolor sit amet consectetur adipiscing elit, Sed do eiusmod tempor incidunt ut labore et dolore magna aliqua...</p>
  <div class="news-input">E-mail</div>
  <a class="btn submit" href="#">SUBMIT HERE</a>
</footer>

</body>
</html>
```